A empresa queria:
" Pista de Tiro indoor, pessoas pagam por ano ou por visita aluguel de pista de tiro aluguel de arma venda de arma venda de munição cursos de tiro Documentação para aquisição de arma CAÇA DE JAVALI "

```html
<!DOCTYPE html>
<html lang="pt-BR">
<head>
<meta charset="UTF-8">
<title>Rocha Alta — Capa Clube de Tiro e Caça</title>
<link rel="stylesheet" href="https://fonts.googleapis.com/css2?family=Russo+One&family=Roboto+Slab:wght@700&family=Roboto:wght@400;500&display=swap">
<style>
  :root {
    --stage: #e4e4e6;
    --panel-dark: #1d1d20;
    --panel-mid: #2a2a2e;
    --brand-red: #d3141b;
    --line-white: #ffffff;
    --text-light: #f2f2f2;
    --text-muted: #c9c9cc;
    --photo-dark: #151517;
    --photo-mid: #4a4b4f;
    --photo-light: #7c7d80;
  }
  * { margin: 0; padding: 0; box-sizing: border-box; }
  html, body { width: 1200px; height: 1200px; overflow: hidden; }
  body {
    background: var(--stage);
    font-family: "Roboto", sans-serif;
    position: relative;
  }
  .profile-badge {
    position: absolute;
    left: 50px; top: 170px;
    width: 280px; height: 280px;
    background: var(--panel-dark);
    display: flex; align-items: center; justify-content: center; gap: 14px;
    box-shadow: 0 6px 20px rgba(0,0,0,.18);
  }
  .profile-badge .mark-dot {
    width: 34px; height: 34px; border-radius: 50%;
    background: var(--brand-red);
  }
  .profile-badge .mark-name {
    font-family: "Russo One", sans-serif;
    color: var(--text-light);
    font-size: 34px; line-height: 1.05;
  }
  .cover {
    position: absolute;
    left: 50px; top: 490px;
    width: 1100px; height: 419px;
    box-shadow: 0 6px 20px rgba(0,0,0,.18);
    overflow: hidden;
  }
  .cover svg { display: block; }
  .brand-name { font-family: "Russo One", sans-serif; font-size: 40px; fill: var(--text-light); }
  .brand-tagline { font-family: "Roboto Slab", serif; font-weight: 700; font-size: 18px; fill: var(--text-light); letter-spacing: 1px; }
  .contact-text { font-family: "Roboto", sans-serif; font-size: 11px; fill: var(--text-muted); }
</style>
</head>
<body>

<div class="profile-badge">
  <span class="mark-dot"></span>
  <span class="mark-name">ROCHA<br>ALTA</span>
</div>

<div class="cover">
  <svg width="1100" height="419" viewBox="0 0 1100 419" xmlns="http://www.w3.org/2000/svg">
    <defs>
      <linearGradient id="panelShade" x1="0" y1="0" x2="1" y2="1">
        <stop offset="0" stop-color="var(--panel-mid)"/>
        <stop offset="1" stop-color="var(--panel-dark)"/>
      </linearGradient>
      <radialGradient id="photoTone" cx="0.55" cy="0.4" r="0.8">
        <stop offset="0" stop-color="var(--photo-light)"/>
        <stop offset="0.45" stop-color="var(--photo-mid)"/>
        <stop offset="1" stop-color="var(--photo-dark)"/>
      </radialGradient>
    </defs>

    <rect class="cover-base" width="1100" height="419" fill="url(#panelShade)"/>

    <g class="photo-side" transform="translate(70 0)">
      <path class="cover-photo" role="img"
            aria-label="Foto de atirador com protetor auricular mirando uma pistola em estande de tiro indoor"
            d="M762 0 H1100 V419 H470 Q478 398 492 380 Z" fill="url(#photoTone)"/>
      <path class="accent-stripe-red" d="M735 0 H750 L478 372 Q466 392 462 419 H446 Q450 388 464 366 Z" fill="var(--brand-red)"/>
      <path class="accent-stripe-white" d="M756 0 H770 L498 376 Q486 396 484 419 H470 Q474 392 488 372 Z" fill="var(--line-white)"/>
    </g>

    <path class="corner-accent-red" d="M0 300 Q40 320 46 370 L52 419 H28 L22 372 Q18 334 0 322 Z" fill="var(--brand-red)"/>
    <path class="corner-accent-white" d="M0 330 Q12 340 14 372 L18 419 H6 L3 376 Q2 352 0 346 Z" fill="var(--line-white)"/>

    <circle class="brand-dot" cx="72" cy="100" r="16" fill="var(--brand-red)"/>
    <text class="brand-name" x="100" y="114">ROCHA ALTA</text>
    <text class="brand-tagline" x="102" y="146">CLUBE DE TIRO E CAÇA</text>

    <g class="contact-row" transform="translate(70 392)">
      <circle cx="5" cy="-4" r="5" fill="var(--text-muted)"/>
      <text class="contact-text" x="15" y="0">(11) 0000-0000</text>
      <path d="M104 -10 q-3 0 -3 3 q1 7 8 9 q3 0 3 -3 l-3 -2 l-2 2 q-3 -1 -4 -4 l2 -2 z" fill="var(--text-muted)"/>
      <text class="contact-text" x="116" y="0">(11) 9000-0000</text>
      <rect x="204" y="-10" width="12" height="8" fill="none" stroke="var(--text-muted)" stroke-width="1.3"/>
      <path d="M204 -10 l6 4.5 l6 -4.5" fill="none" stroke="var(--text-muted)" stroke-width="1.3"/>
      <text class="contact-text" x="221" y="0">contato@rochaalta.com</text>
      <circle cx="347" cy="-4" r="5" fill="var(--text-muted)"/>
      <text class="contact-text" x="357" y="0">rochaalta.com</text>
    </g>
  </svg>
</div>

</body>
</html>
```